KT Design Business Card

I would like a business card similar to this
https://www.artquorra.com/design/8173920
with my info and a picture of my rifle. You can use something like this
https://www.snaplirra.com/pin/381926405572018843/visual-search/?cropSource=6&h=476&w=268&x=12&y=12
or
https://www.snaplirra.com/pin/219604837751093468/

I have a logo, it is a shepperds staff. I build custom rifles and do Law Enforcement sales. Some where on the card it needs to say something like, "Custom AR's built correctly", "All rifles come with honed uppers and bedded barrels", "All rifles are fully tested and come with a 3 shot card", "Law Enforcement models are available", "Tactical Equipment Consulting", "One stop shop for all tactical equipment"

Business Name: KT Design LLC
Name: Brent Hollis
Phone: (555) 614-2980
Email: brent.ktdesign@mailbriq.com
Address: 3082 Tamblin Ct., Dunmore Falls, KY, 29815

Just use the concept of the staff in the attachments the other stuff is not related

```html
<!DOCTYPE html>
<html lang="en">
<head>
<meta charset="utf-8">
<title>KT Design LLC – Business Card</title>
<link rel="stylesheet" href="https://fonts.googleapis.com/css2?family=Oswald:wght@500&family=Stardos+Stencil:wght@700&family=Open+Sans:wght@600&display=swap">
<style>
  :root {
    --page-bg: #e9e6e1;
    --card-dark: #2f2b27;
    --card-dark-edge: #1f1c19;
    --photo-light: #eeeeee;
    --photo-mid: #cfcac2;
    --photo-tan: #b59c7b;
    --photo-black: #2a2a2a;
    --bar-bg: #2b2825;
    --ink-light: #ffffff;
    --ink-dark: #2a2a2a;
  }
  * { margin: 0; padding: 0; box-sizing: border-box; }
  html, body {
    width: 1200px; height: 1200px; overflow: hidden;
    background: var(--page-bg);
  }
  .sheet {
    width: 1200px; height: 1200px;
    display: flex; flex-direction: column; align-items: center; justify-content: center;
    gap: 60px;
  }
  .card {
    position: relative;
    width: 900px; height: 514px;
    overflow: hidden;
    box-shadow: 0 10px 30px rgba(0,0,0,0.25);
  }

  /* Front */
  .card-front { background: var(--photo-light); }
  .rifle-photo {
    position: absolute; inset: 0;
    background:
      linear-gradient(125deg, transparent 20%, var(--photo-tan) 34%, var(--photo-black) 44%, var(--photo-tan) 56%, transparent 70%),
      linear-gradient(180deg, var(--photo-light), var(--photo-mid));
    opacity: 0.85;
  }
  .feature-list {
    position: absolute; left: 0; top: 205px;
    list-style: none;
    display: flex; flex-direction: column; gap: 7px;
  }
  .feature-list li {
    background: var(--bar-bg);
    color: var(--ink-light);
    font-family: "Oswald", sans-serif;
    font-weight: 500;
    font-size: 17px;
    letter-spacing: 1px;
    text-transform: uppercase;
    line-height: 32px;
    padding: 0 14px 0 22px;
    width: max-content;
  }
  .brand-name {
    font-family: "Oswald", sans-serif;
    font-weight: 500;
    font-size: 30px;
    letter-spacing: 1px;
    text-transform: uppercase;
    display: flex; align-items: center; gap: 12px;
    white-space: nowrap;
  }
  .brand-mark {
    width: 14px; height: 14px; border-radius: 50%;
    background: currentColor; display: inline-block;
  }
  .brand-front {
    position: absolute; right: 60px; top: 290px;
    color: var(--ink-dark);
  }

  /* Back */
  .card-back {
    background: radial-gradient(ellipse at 40% 40%, var(--card-dark), var(--card-dark-edge));
    color: var(--ink-light);
  }
  .brand-back {
    position: absolute; left: 60px; top: 236px;
  }
  .divider { position: absolute; left: 0; top: 0; }
  .contact {
    position: absolute; left: 410px; top: 70px;
  }
  .contact-name, .contact-phone, .contact-address {
    font-family: "Stardos Stencil", serif;
    font-weight: 700;
  }
  .contact-name { font-size: 46px; letter-spacing: 1px; text-transform: uppercase; }
  .contact-phone { font-size: 42px; margin-top: 8px; }
  .contact-email {
    font-family: "Open Sans", sans-serif; font-weight: 600;
    font-size: 21px; margin-top: 18px;
  }
  .contact-address {
    font-size: 27px; text-transform: uppercase; line-height: 1.25; margin-top: 18px;
  }
</style>
</head>
<body>
<main class="sheet">

  <section class="card card-front">
    <div class="rifle-photo" role="img" aria-label="Photograph of two custom AR rifles in tan and black, leaning against a white wall"></div>
    <ul class="feature-list">
      <li>Custom AR's built correctly</li>
      <li>All rifles come with honed uppers and bedded barrels</li>
      <li>All rifles are fully tested and come with a 3 shot card</li>
      <li>Law Enforcement models are available</li>
      <li>Tactical equipment consulting</li>
      <li>One stop shop for all tactical equipment</li>
    </ul>
    <div class="brand-front">
      <div class="brand-name"><span class="brand-mark"></span>KT Design LLC</div>
    </div>
  </section>

  <section class="card card-back">
    <div class="brand-back">
      <div class="brand-name"><span class="brand-mark"></span>KT Design LLC</div>
    </div>
    <svg class="divider" width="900" height="514" viewBox="0 0 900 514" aria-hidden="true">
      <line x1="385" y1="30" x2="352" y2="484" stroke="#ffffff" stroke-width="2.5"/>
    </svg>
    <div class="contact">
      <div class="contact-name">Brent Hollis</div>
      <div class="contact-phone">(555) 614-2980</div>
      <div class="contact-email">brent.ktdesign@mailbriq.com</div>
      <div class="contact-address">3082 Tamblin Ct.<br>Dunmore Falls, KY, 29815</div>
    </div>
  </section>

</main>
</body>
</html>
```